Save the date for wedding

A save the date for our wedding. We're looking for a simple and sleek invite. I would prefer not alot of calligraphy. Minimalism is good. The basic info to include is as follows:
Names: Mona and Felix
Date: June 9th
Where: Ottawa, Ontario
In small print please include that there will be a reception in Edmonton AB September 1st for those who cannot make it to Ottawa.
Please see the attached file for a style idea. Doesn’t have to be exactly like that, but something like that.

```html
<!DOCTYPE html>
<html lang="en">
<head>
<meta charset="UTF-8">
<title>Mona and Felix – Save the Date</title>
<link rel="stylesheet" href="https://fonts.googleapis.com/css2?family=Mr+Dafoe&family=Lora:wght@400;600&display=swap">
<style>
  :root {
    --paper: #fdfcf4;
    --gold: #dcbb5c;
    --ink-grey: #5a5a5a;
    --band: #666666;
    --band-text: #ffffff;
  }
  html, body {
    margin: 0;
    padding: 0;
    width: 1200px;
    height: 851px;
    overflow: hidden;
    background: var(--paper);
  }
  .save-the-date {
    position: relative;
    width: 1200px;
    height: 851px;
    background: var(--paper);
  }
  .couple-name {
    position: absolute;
    left: 0;
    width: 100%;
    margin: 0;
    text-align: center;
    font-family: "Mr Dafoe", cursive;
    font-weight: 400;
    color: var(--gold);
    line-height: 1;
  }
  .couple-name--first {
    top: 30px;
    font-size: 290px;
  }
  .couple-name--second {
    top: 380px;
    font-size: 290px;
  }
  .conjunction {
    position: absolute;
    top: 352px;
    left: 0;
    width: 100%;
    margin: 0;
    text-align: center;
    font-family: "Lora", serif;
    font-weight: 600;
    font-size: 46px;
    color: var(--ink-grey);
    line-height: 1;
  }
  .details-band {
    position: absolute;
    left: 0;
    bottom: 0;
    width: 100%;
    height: 138px;
    background: var(--band);
    text-align: center;
  }
  .event-line {
    margin: 0;
    padding-top: 24px;
    font-family: "Lora", serif;
    font-size: 36px;
    letter-spacing: 4px;
    color: var(--band-text);
    text-transform: uppercase;
    line-height: 1.2;
  }
  .event-line .separator {
    margin: 0 14px;
  }
  .reception-note {
    margin: 16px 0 0;
    font-family: "Lora", serif;
    font-size: 23px;
    color: var(--gold);
    line-height: 1.2;
  }
</style>
</head>
<body>
  <main class="save-the-date">
    <h1 class="couple-name couple-name--first">Mona</h1>
    <p class="conjunction">and</p>
    <h1 class="couple-name couple-name--second">Felix</h1>
    <section class="details-band">
      <p class="event-line">June 9, 2018<span class="separator">•</span>Ottawa, Ontario</p>
      <p class="reception-note">Reception in Edmonton AB September 1st for those who cannot make it to Ottawa.</p>
    </section>
  </main>
</body>
</html>
```